Brindle Structures Construction Company Seeking Modern Website

We are a small construction company wanting to create a web presence. We don't have much in the way of current content but will get photos as they come in. Attached is a picture of our business card.
The pages we would like on the menu are:
Home
Portfolio
Product Specs
Testimonials
Our Process
Contact
Some designs we like are:
http://www.tovenquarnsheds.example/
http://www.qzrsheds.example/
http://pannowsheds.example/
http://wistenhalls.example/
Not much requirements other than that so feel free to be creative!
Updates
Target Market(s)
Construction
Commercial and Residential Buildings
Industry/Entity Type
Construction Company
Number of Pages Required
5+ page
Look and feel

```html
<!DOCTYPE html>
<html lang="en">
<head>
<meta charset="utf-8">
<title>Brindle Structures</title>
<link href="https://fonts.googleapis.com/css2?family=Open+Sans:wght@400;600;700;800&display=swap" rel="stylesheet">
<style>
:root{
  --yellow:#f4c04a;
  --yellow-deep:#e9ad22;
  --yellow-soft:#f8d679;
  --ink:#3a3a3a;
  --text:#555;
  --muted:#888;
  --dark:#2a2a2a;
  --white:#fff;
  --tool-grey:#e3e3e3;
}
*{box-sizing:border-box;margin:0;padding:0}
html,body{width:1200px;height:4945px;overflow:hidden;background:var(--white)}
body{font-family:'Open Sans',Arial,sans-serif;color:var(--text)}
.page{position:relative;width:1200px;height:4945px;overflow:hidden}
.abs{position:absolute}
/* header */
.topbar{left:0;top:0;width:1200px;height:90px;background:var(--white)}
.brand{left:110px;top:14px;font-size:34px;font-weight:800;color:#1e5fb0;display:flex;align-items:center;gap:10px}
.brand i{width:18px;height:18px;background:var(--yellow);display:block}
.contact-top{right:110px;top:30px;display:flex;gap:40px;font-size:16px;color:var(--ink)}
.contact-top span{display:flex;align-items:center;gap:10px}
.nav{left:0;top:90px;width:1200px;height:98px;background:var(--white);border-top:1px solid #eee}
.nav ul{list-style:none;display:flex;position:absolute;left:110px;top:0;height:98px;align-items:center}
.nav li{font-size:17px;font-weight:800;color:#222;padding:0 22px;letter-spacing:.5px}
.nav li.active{background:var(--yellow);height:130px;margin-top:-32px;display:flex;align-items:center;padding:30px 38px 0;clip-path:polygon(0 0,100% 0,100% 88%,50% 100%,0 88%)}
/* hero */
.hero{left:0;top:188px;width:1200px;height:702px;background:linear-gradient(120deg,#8a6a40 0%,#b88f5c 35%,#6d5234 70%,#3f2f20 100%)}
.hero-panel{left:224px;top:152px;width:760px;height:460px;background:rgba(30,30,30,.72);text-align:center;color:var(--white)}
.hero-panel .welcome{margin-top:100px;font-size:36px;letter-spacing:12px;font-weight:400}
.hero-panel h1{font-size:56px;font-weight:700;letter-spacing:5px;line-height:1.1}
.hero-panel h2{font-size:22px;font-weight:700;letter-spacing:2px;margin-top:4px}
.hero-panel p{font-size:16px;margin:30px auto 0;width:600px;line-height:1.4}
.hero-btn{display:inline-block;margin-top:52px;border:2px solid var(--white);border-left:10px solid var(--yellow);padding:8px 34px;font-size:16px;font-weight:700;letter-spacing:2px}
.arrow{top:430px}
/* section heads */
.band{left:0;width:1200px;background:linear-gradient(180deg,var(--yellow-soft),var(--yellow))}
.title{width:1200px;left:0;text-align:center;font-size:44px;font-weight:700;letter-spacing:4px;color:var(--yellow)}
.title.light{color:var(--white)}
.sub{width:1200px;left:0;text-align:center;font-size:16px;color:var(--ink);line-height:1.5}
/* gallery */
.tile{width:311px;height:286px}
.tile-feature{background:rgba(244,192,74,.85);color:var(--white)}
.tile-feature b{position:absolute;left:8px;top:10px;font-size:18px}
.tile-feature span{position:absolute;right:14px;bottom:8px;font-size:17px;font-weight:600}
/* specs */
.specs-text{left:110px;width:980px;text-align:center;font-size:17px;line-height:1.5;color:var(--ink)}
.structure{left:110px;top:2345px;font-size:24px;font-weight:700;color:var(--yellow);letter-spacing:1px}
.bullets{left:110px;top:2395px;width:720px;list-style:none;font-size:16px;color:var(--ink);line-height:1.55}
.bullets li{padding-left:24px;position:relative;margin-bottom:3px}
.bullets li::before{content:"";position:absolute;left:2px;top:8px;width:10px;height:10px;background:var(--yellow)}
.tools-strip{left:0;width:1200px;height:122px;background:linear-gradient(90deg,#f2f2f2,var(--tool-grey),#f2f2f2)}
/* team */
.member{width:231px;height:346px}
.member .photo{height:246px;background:linear-gradient(160deg,#f6d77a,var(--yellow))}
.member.dark .photo{background:linear-gradient(160deg,#3a3a3a,#111)}
.member .label{height:100px;background:var(--yellow);color:var(--white);text-align:center;padding-top:24px;border:3px solid var(--white)}
.member.dark .label{background:#111}
.member .label b{display:block;font-size:17px;letter-spacing:1px}
.member .label span{font-size:15px;letter-spacing:1px}
/* process */
.proc{width:462px;height:307px;display:flex}
.proc .info{width:230px;background:var(--yellow);color:var(--white);padding:30px 16px}
.proc .info h3{font-size:17px;text-align:center}
.proc .info p{font-size:15px;margin-top:24px;line-height:1.4}
.proc .bar{margin-top:52px;height:10px;background:var(--white);border-radius:5px;overflow:hidden}
.proc .bar i{display:block;height:100%;background:#d9d9d9;margin-left:auto}
.proc .meta{display:flex;justify-content:space-between;font-size:12px;margin-top:6px}
.proc .pic{flex:1;background:linear-gradient(180deg,#9cc3e6,#b8895a 60%,#6a4a2a)}
/* testimonials */
.quote-text{left:130px;width:940px;text-align:center;font-size:16px;line-height:1.5;color:var(--ink)}
.dots{left:570px;top:4575px;display:flex;gap:6px}
.dots i{width:16px;height:16px;border:2px solid #222;display:block}
.dots i.on{background:#222}
/* footer */
.footer{left:0;top:4615px;width:1200px;height:330px;background:var(--dark);color:var(--white)}
.footer h4{font-size:26px;font-weight:700;letter-spacing:2px;border-bottom:3px solid var(--white);display:inline-block;padding-bottom:2px}
.footer p,.footer li{font-size:17px;line-height:1.5;color:#ddd}
.footer ul{list-style:none;margin-top:22px}
.footer li{display:flex;gap:12px;align-items:flex-start;margin-bottom:8px}
.social{display:flex;gap:10px;margin-top:24px}
.social i{width:34px;height:34px;background:var(--yellow);display:block}
</style>
</head>
<body>
<div class="page">
  <header>
    <div class="abs topbar"></div>
    <div class="abs brand"><i></i>Brindle Structures</div>
    <div class="abs contact-top">
      <span><svg width="14" height="20" viewBox="0 0 14 20"><rect x="1" y="1" width="12" height="18" rx="2" fill="none" stroke="#222" stroke-width="2"/><circle cx="7" cy="15.5" r="1.3" fill="#222"/></svg>1-888-123-4567</span>
      <span><svg width="20" height="14" viewBox="0 0 20 14"><rect width="20" height="14" fill="#222"/><path d="M0 0l10 8 10-8" stroke="#fff" stroke-width="1.5" fill="none"/></svg>info@example.com</span>
    </div>
    <nav class="abs nav"><ul>
      <li class="active">HOME</li><li>PORTFOLIO</li><li>PRODUCT SPECS</li><li>TESTIMONIALS</li><li>OUR PROCESS</li><li>CONTACT</li>
    </ul></nav>
  </header>

  <section class="abs hero" role="img" aria-label="Hard hat and tools resting on wooden planks">
    <svg class="abs arrow" style="left:100px" width="40" height="50" viewBox="0 0 40 50"><path d="M32 4L8 25l24 21" stroke="#fff" stroke-width="9" fill="none"/></svg>
    <svg class="abs arrow" style="left:1060px" width="40" height="50" viewBox="0 0 40 50"><path d="M8 4l24 21L8 46" stroke="#fff" stroke-width="9" fill="none"/></svg>
    <div class="abs hero-panel">
      <div class="welcome">WELCOME TO</div>
      <h1>BRINDLE STRUCTURES</h1>
      <h2>WE ARE CONSTRUCTION COMPANY</h2>
      <p>We aim to eliminate the task of dividing your project between different architecture and construction company</p>
      <div class="hero-btn">CONTACT US</div>
    </div>
  </section>

  <section>
    <div class="abs band" style="top:890px;height:287px" role="img" aria-label="Faint building blueprint on yellow"></div>
    <h2 class="abs title light" style="top:968px">PROJECTS</h2>
    <div class="abs sub" style="top:1040px;color:#fff;letter-spacing:2px;font-size:15px">LET'S TAKE A LOOK AT OUR BEST &amp; BIG PROJECTS</div>

    <div class="abs tile" style="left:119px;top:1226px;background:linear-gradient(180deg,#a9cdee,#c8c0b0 55%,#6f9a4a)" role="img" aria-label="Two-storey suburban house"></div>
    <div class="abs tile" style="left:435px;top:1226px;background:linear-gradient(180deg,#b6d3ee,#e6ded0 55%,#7a9a5a)" role="img" aria-label="Modern white villa"></div>
    <div class="abs tile" style="left:758px;top:1226px;background:linear-gradient(180deg,#cfe0ef,#8a6a4a 55%,#5a6a4a)" role="img" aria-label="Timber-clad modern house"></div>
    <div class="abs tile" style="left:119px;top:1520px;background:linear-gradient(180deg,#5f9fd8,#c9a06a 55%,#3b6f8f)" role="img" aria-label="Modern house with pool"></div>
    <div class="abs tile tile-feature" style="left:435px;top:1520px;background:linear-gradient(180deg,#f0cd72,#e8b84a)" role="img" aria-label="Contemporary villa project">
      <b>Contemporary Villa</b>
      <svg class="abs" style="left:130px;top:118px" width="50" height="50" viewBox="0 0 50 50"><circle cx="21" cy="21" r="14" fill="none" stroke="#fff" stroke-width="4"/><path d="M31 31l14 14" stroke="#fff" stroke-width="5"/></svg>
      <span>View Project</span>
    </div>
    <div class="abs tile" style="left:758px;top:1520px;background:linear-gradient(180deg,#23355e,#3a5a8a 50%,#d8a060)" role="img" aria-label="Modern house at dusk"></div>
    <div class="abs tile" style="left:119px;top:1820px;background:linear-gradient(180deg,#c9dfef,#c89a5e 50%,#8a6236)" role="img" aria-label="Builder on timber frame"></div>
    <div class="abs tile" style="left:435px;top:1820px;background:linear-gradient(180deg,#d2e3ef,#c8a070 50%,#9a7448)" role="img" aria-label="Timber frame under construction"></div>
    <div class="abs tile" style="left:758px;top:1820px;background:linear-gradient(180deg,#8fbfe8,#c4a27a 60%,#8a6a48)" role="img" aria-label="Worker on roof trusses"></div>
  </section>

  <section>
    <h2 class="abs title" style="top:2160px">PRODUCT SPECS</h2>
    <p class="abs specs-text" style="top:2245px">Harlowe Post Buildings offers the following high quality standard specifications as the minimum standards to which all our buildings are constructed. Because we offer full customization, you may request additional features as well.</p>
    <div class="abs structure">STRUCTURE</div>
    <ul class="abs bullets">
      <li>Laminated posts a full four feet in the ground, set on an engineered concrete "cookie"</li>
      <li>Engineered trusses custom designed to National Building Code wind and snow load requirements for your area</li>
      <li>Treated 2 x 8 at the ground level</li>
      <li>Bracing to Engineer's specifications and "hurricane tied" to the posts</li>
      <li>Double header beam, one on the inside and one on the outside of your posts</li>
      <li>One foot overhangs all the way around your structure</li>
    </ul>
    <div class="abs" style="left:818px;top:2330px;width:342px;height:310px;border-radius:50%;background:radial-gradient(circle,#c9c9c9,#e8b84a 55%,#ffffff 72%)" role="img" aria-label="Assorted hand and power tools"></div>
    <div class="abs tools-strip" style="top:2710px" role="img" aria-label="Faint row of tool silhouettes"></div>
  </section>

  <section>
    <h2 class="abs title" style="top:2895px">TEAM MEMBERS</h2>
    <p class="abs sub" style="top:2990px;left:200px;width:800px">We're Some Creative People with Powerful Knowledge &amp; Skills Behind the Scene Bringing You the Bests</p>
    <div class="abs member dark" style="left:119px;top:3132px"><div class="photo" role="img" aria-label="Architect portrait"></div><div class="label"><b>TOBIN VARRICK</b><span>ARCHITECT</span></div></div>
    <div class="abs member" style="left:363px;top:3132px"><div class="photo" role="img" aria-label="Supervisor portrait"></div><div class="label"><b>ELDEN MARSH</b><span>SUPERVISOR</span></div></div>
    <div class="abs member" style="left:607px;top:3132px"><div class="photo" style="background:linear-gradient(160deg,#fff,#eee)" role="img" aria-label="Manager portrait"></div><div class="label"><b>CORINNE ALBANY</b><span>MANAGER</span></div></div>
    <div class="abs member" style="left:851px;top:3132px"><div class="photo" style="background:linear-gradient(160deg,#fff,#eee)" role="img" aria-label="Civil engineer portrait"></div><div class="label"><b>NEVILLE OAKHURST</b><span>CIVIL ENGINEER</span></div></div>
    <div class="abs tools-strip" style="top:3538px" role="img" aria-label="Faint row of tool silhouettes"></div>
  </section>

  <section>
    <h2 class="abs title" style="top:3705px">OUR PROCESS</h2>
    <p class="abs sub" style="top:3778px;left:200px;width:800px">We're Currently Working on Some Big Projects, Our Specialists Are Trying Their Bests to Complete Them ASAP.</p>
    <div class="abs proc" style="left:125px;top:3890px">
      <div class="info"><h3>Green House</h3><p>Proin sagittis feugiat elit finibus pretium. Donec et tortor non.</p>
        <div class="bar"><i style="width:45%"></i></div><div class="meta"><span>COMPLETION</span><span>55%</span></div></div>
      <div class="pic" role="img" aria-label="House frame under construction"></div>
    </div>
    <div class="abs proc" style="left:620px;top:3890px">
      <div class="info"><h3>Green House</h3><p>Proin sagittis feugiat elit finibus pretium. Donec et tortor non.</p>
        <div class="bar"><i style="width:25%"></i></div><div class="meta"><span>COMPLETION</span><span>75%</span></div></div>
      <div class="pic" style="background:linear-gradient(180deg,#c9d9c0,#8a5a38 55%,#5a3a22)" role="img" aria-label="Timber cabin nearing completion"></div>
    </div>
  </section>

  <section>
    <div class="abs band" style="top:4243px;height:372px" role="img" aria-label="Faint building blueprint on yellow"></div>
    <h2 class="abs title light" style="top:4262px">TESTIMONIALS</h2>
    <svg class="abs" style="left:572px;top:4330px" width="56" height="46" viewBox="0 0 56 46"><path d="M0 46V24Q0 4 22 0v9Q10 12 10 22h12v24zM32 46V24Q32 4 54 0v9Q42 12 42 22h12v24z" fill="#222"/></svg>
    <p class="abs quote-text" style="top:4395px">I am very pleased with the building that Harlowe put together for me, and especially with how they handled the details for me. The crew that assembled my building was professional and paid attention to detail and the quality of their work. Considering I will look at this building for a long time, I am grateful it was done properly without a complaint from myself. Every big project has a few hiccups, and any and all issues were addressed by the project manager</p>
    <div class="abs dots"><i></i><i class="on"></i><i></i></div>
  </section>

  <footer class="abs footer">
    <div class="abs" style="left:110px;top:30px;width:260px">
      <h4>ABOUT US</h4>
      <p style="margin-top:18px">Lorem ipsum dolor sit amet, consectetur adipiscing elit. Quisque nec erat erat, er blandit, nulla quis fermentum, orem ipsum dolor sit amet, consectetur adipiscing elit.</p>
    </div>
    <div class="abs" style="left:490px;top:30px;width:300px">
      <h4>OUR CONTACT</h4>
      <ul>
        <li><svg width="14" height="20" viewBox="0 0 14 20" style="margin-top:4px"><path d="M7 0a7 7 0 0 1 7 7c0 5-7 13-7 13S0 12 0 7a7 7 0 0 1 7-7z" fill="#fff"/><circle cx="7" cy="7" r="2.5" fill="#2a2a2a"/></svg><span>Brindle Structures<br>P.O. Box 204,<br>Larkmoor IN 40000</span></li>
        <li><svg width="14" height="20" viewBox="0 0 14 20" style="margin-top:4px"><rect x="1" y="1" width="12" height="18" rx="2" fill="none" stroke="#fff" stroke-width="2"/></svg>1-888-123-4567</li>
        <li><svg width="18" height="13" viewBox="0 0 18 13" style="margin-top:6px"><rect width="18" height="13" fill="#fff"/><path d="M0 0l9 7 9-7" stroke="#2a2a2a" stroke-width="1.5" fill="none"/></svg>info@example.com</li>
      </ul>
    </div>
    <div class="abs" style="left:925px;top:30px">
      <h4>FOLLOW US</h4>
      <div class="social" style="justify-content:center"><i></i><i></i><i></i></div>
    </div>
  </footer>
</div>
</body>
</html>
```